Appraisal and Umpire Services for Property Damage Insurance Claims

I need a banner design that I can post as an advertisement on industry web pages. I would like this to be elegant and reflective of quality, integrity and professionalism.

Target Market(s)

Insurance Companies and Attorneys

Industry/Entity Type

Insurance

Contact Information for Business Card

Gerald M. Hollis
918 Birchwell Lane
PO Box 582
Clifton Park, NY 12093
ghollis@brindlevault.com
Phone: (800) 555-0147, Ext. 2861
Direct: (315) 555-0189

Logo Text

Line One: Velmar Brook Claim Service, Inc. Line two: Appraisal and Umpire Services

Font styles to use
Serif
Sans Serif

Colors
0255a3
f78f20
faa54b
3176b5

Requirements
Must have
• New Logo and matching banner, business card and stationary.
• The colors must be orange and navy blue in the logo. I have selected them below.

```html
<!DOCTYPE html>
<html lang="en">
<head>
<meta charset="utf-8">
<title>Velmar Brook Claim Service – Appraisal &amp; Umpire Services</title>
<link href="https://fonts.googleapis.com/css2?family=Montserrat:wght@300;400;500;600;700&display=swap" rel="stylesheet">
<style>
  :root {
    --navy: #252b66;
    --navy-deep: #23295f;
    --orange: #f78f20;
    --orange-light: #faa54b;
    --blue: #3176b5;
    --white: #ffffff;
    --rule: #9a9cb8;
  }
  * { margin: 0; padding: 0; box-sizing: border-box; }
  html, body { width: 1200px; height: 2400px; overflow: hidden; background: var(--white); }
  .banner {
    position: relative;
    width: 1200px;
    height: 2400px;
    background: var(--white);
    font-family: "Montserrat", sans-serif;
    color: var(--navy);
    overflow: hidden;
  }
  .brand {
    position: absolute;
    top: 118px;
    left: 0;
    width: 100%;
    text-align: center;
    color: var(--navy);
    font-weight: 600;
  }
  .brand-name {
    font-size: 100px;
    letter-spacing: 2px;
    line-height: 1;
  }
  .brand-sub {
    margin-top: 22px;
    font-size: 44px;
    letter-spacing: 5px;
    line-height: 1;
  }
  .hero {
    position: absolute;
    top: 330px;
    left: 0;
    width: 1200px;
    height: 1060px;
  }
  .services {
    position: absolute;
    top: 1390px;
    left: 76px;
    width: 1080px;
    height: 360px;
  }
  .accent-bar {
    position: absolute;
    left: 0;
    top: 10px;
    width: 10px;
    height: 330px;
    background: linear-gradient(to bottom, var(--navy) 0 50%, var(--orange-light) 50% 100%);
  }
  .headline {
    position: absolute;
    left: 42px;
    top: 0;
    font-size: 90px;
    font-weight: 400;
    line-height: 118px;
    color: var(--navy);
  }
  .divider {
    position: absolute;
    left: 554px;
    top: 12px;
    width: 4px;
    height: 330px;
    background: var(--rule);
  }
  .service-list {
    position: absolute;
    left: 596px;
    top: 22px;
    list-style: none;
    font-size: 44px;
    font-weight: 400;
    letter-spacing: 2px;
    line-height: 94px;
    color: var(--navy);
  }
  .service-list li.two-line { line-height: 56px; padding-top: 20px; }
  .cta {
    position: absolute;
    left: 312px;
    top: 1898px;
    width: 576px;
    height: 122px;
    border-radius: 14px;
    background: linear-gradient(to bottom, #ffc24a 0%, #f9a21c 55%, #f39312 100%);
    color: var(--white);
    font-size: 64px;
    font-weight: 500;
    line-height: 122px;
    text-align: center;
    text-decoration: none;
  }
  .phone-band {
    position: absolute;
    left: 0;
    bottom: 0;
    width: 1200px;
    height: 288px;
    background: var(--navy-deep);
    color: var(--white);
    font-size: 88px;
    font-weight: 600;
    line-height: 288px;
    text-align: center;
    letter-spacing: 1px;
  }
</style>
</head>
<body>
<main class="banner">
  <header class="brand">
    <div class="brand-name">VELMAR BROOK</div>
    <div class="brand-sub">CLAIM SERVICE, INC</div>
  </header>

  <svg class="hero" viewBox="0 0 1200 1060" xmlns="http://www.w3.org/2000/svg">
    <defs>
      <linearGradient id="heroTones" x1="0" y1="0" x2="1" y2="1">
        <stop offset="0" stop-color="#8a8f86"/>
        <stop offset="0.35" stop-color="#6f7b74"/>
        <stop offset="0.65" stop-color="#8e8478"/>
        <stop offset="1" stop-color="#5f6d78"/>
      </linearGradient>
      <linearGradient id="heroFade" x1="0" y1="0" x2="0" y2="1">
        <stop offset="0" stop-color="#ffffff" stop-opacity="1"/>
        <stop offset="0.2" stop-color="#ffffff" stop-opacity="0.3"/>
        <stop offset="0.35" stop-color="#ffffff" stop-opacity="0"/>
      </linearGradient>
    </defs>
    <rect role="img" aria-label="Aerial view of a storm-damaged neighbourhood with torn roofs and debris" x="0" y="0" width="1200" height="1060" fill="url(#heroTones)"/>
    <rect x="0" y="0" width="1200" height="1060" fill="url(#heroFade)"/>
    <path d="M0 1060 L0 990 Q520 990 1200 800 L1200 1060 Z" fill="#ffffff"/>
    <path d="M420 1000 Q820 960 1200 800 L1200 826 Q820 990 420 1000 Z" fill="var(--orange)"/>
  </svg>

  <section class="services">
    <div class="accent-bar"></div>
    <h1 class="headline">Appraisal<br>&amp; Umpire<br>Services</h1>
    <div class="divider"></div>
    <ul class="service-list">
      <li>PROPERTY</li>
      <li>CASUALTY</li>
      <li class="two-line">CLAIM<br>ADMINISTRATION</li>
    </ul>
  </section>

  <a class="cta" href="#">Learn More</a>

  <footer class="phone-band">1-800-555-0147</footer>
</main>
</body>
</html>
```